Business card for Eyelash extension salon in Beverly Hills,California USA

We need new business card for our salon in Beverly Hills. The salon name is 'Lashvora' . We would like to have...Business name: Lashvora Name of person: will provide later Address 6812 N.Calder Ridge Ave Beverly Hills , CA 90210 Phone: will provide later (Text only) Web: www.lashvorastudio-demo.com Instagram icon, Facebook icon follow us for seasonal campaign and news @lashvorastudiodemo Design should look elegant, high-end, clean, simple, cohesive with my brand. Please refer my brand board. Business name color will be metallic bronzy color. Im thinking grey background or white background. Thanks

Target Market(s)

25-35. Gender neutral. People who are in Entertainment business industry.
This is High-end Eyelash extension salon in Beverly Hills

Industry/Entity Type

Beauty Salon

Contact Information for Business Card

Business name: Lashvora
Name of person: will provide later
Address 6812 N.Calder Ridge Ave Beverly Hills , CA 90210
Phone: will provide later (Text only)
Web: www.lashvorastudio-demo.com
Instagram icon, Facebook icon
follow us for seasonal campaign and news @lashvorastudiodemo

Requirements
Must have
• Beautiful, elegant, clean and simple look but very attractive and modern
Should not have
• We don't like too clutter, too busy designs.

```html
<!DOCTYPE html>
<html lang="en">
<head>
<meta charset="utf-8">
<title>Lashvora Business Card</title>
<link href="https://fonts.googleapis.com/css2?family=Libre+Baskerville:wght@400;700&family=Montserrat:wght@500&display=swap" rel="stylesheet">
<style>
  :root {
    --canvas: #e8e8e8;
    --card: #ffffff;
    --marble-light: #f7f7f7;
    --marble-vein: #cfcfcf;
    --band: rgba(255, 255, 255, 0.82);
    --ink: #111111;
    --rule: #1a1a1a;
    --divider: #9a9a9a;
    --shadow: rgba(0, 0, 0, 0.12);
  }
  * { box-sizing: border-box; margin: 0; padding: 0; }
  html, body {
    width: 1200px; height: 800px; overflow: hidden;
    background: var(--canvas);
  }
  .canvas {
    position: relative; width: 1200px; height: 800px;
    font-family: "Libre Baskerville", Georgia, serif;
    color: var(--ink);
  }
  .card {
    position: absolute; width: 540px; height: 309px;
    background: var(--card);
    box-shadow: 0 6px 18px var(--shadow);
    overflow: hidden;
  }
  .card--back { left: 600px; top: 70px; }
  .card--front { left: 60px; top: 410px; }
  .card__marble {
    position: absolute; inset: 0;
    background:
      linear-gradient(160deg, transparent 0 20%, var(--marble-vein) 22%, transparent 26% 60%, var(--marble-vein) 62%, transparent 66%),
      linear-gradient(30deg, var(--marble-light), #ececec 40%, var(--marble-light) 70%, #e4e4e4);
    opacity: 0.9;
  }
  .card__band {
    position: absolute; left: 0; right: 0; top: 58px; height: 190px;
    background: var(--band);
  }
  .card__frame {
    position: absolute; inset: 22px;
    border: 1.5px solid var(--rule);
  }
  .brand { text-align: center; }
  .brand__name {
    font-size: 44px; font-weight: 400; letter-spacing: 1px; line-height: 1;
  }
  .brand__place {
    font-family: "Montserrat", Arial, sans-serif; font-weight: 500;
    font-size: 7px; letter-spacing: 2.5px; margin-top: 8px;
  }
  .card--back .brand {
    position: absolute; left: 0; right: 0; top: 108px;
  }
  .card--back .web {
    position: absolute; left: 0; right: 0; top: 196px;
    text-align: center; font-size: 12px; font-weight: 700; letter-spacing: 0.5px;
  }
  .card--front .brand {
    position: absolute; left: 40px; width: 220px; top: 98px;
  }
  .card--front .brand__name { font-size: 38px; }
  .address {
    position: absolute; left: 40px; right: 40px; bottom: 36px;
    font-size: 12px; text-align: left; padding-left: 16px;
  }
  .divider {
    position: absolute; left: 280px; top: 80px; width: 1px; height: 140px;
    background: var(--divider);
  }
  .contact {
    position: absolute; left: 300px; top: 84px; font-size: 12px; line-height: 1.35;
  }
  .contact__name { font-size: 20px; font-weight: 700; }
  .contact__role { font-size: 12px; margin-bottom: 10px; }
  .social {
    display: flex; align-items: center; gap: 5px; margin-top: 6px;
  }
  .social__box {
    width: 14px; height: 14px; border: 1.2px solid var(--ink); border-radius: 2px;
  }
</style>
</head>
<body>
<main class="canvas">

  <section class="card card--back" aria-label="Card back">
    <div class="card__marble" role="img" aria-label="White marble texture with soft grey veins"></div>
    <div class="card__band"></div>
    <div class="card__frame"></div>
    <div class="brand">
      <div class="brand__name">Lashvora</div>
      <div class="brand__place">BEVERLY HILLS</div>
    </div>
    <div class="web">www.lashvorastudio-demo.com</div>
  </section>

  <section class="card card--front" aria-label="Card front">
    <div class="card__marble" role="img" aria-label="White marble texture with soft grey veins"></div>
    <div class="card__band"></div>
    <div class="card__frame"></div>
    <div class="brand">
      <div class="brand__name">Lashvora</div>
      <div class="brand__place">BEVERLY HILLS</div>
    </div>
    <div class="divider"></div>
    <div class="contact">
      <div class="contact__name">Mara Ellison</div>
      <div class="contact__role">Owner</div>
      <div>P: +1 310 555 0148</div>
      <div>E: hello@lashvora-mail.demo</div>
      <div class="social">
        <span class="social__box"></span>
        <span class="social__box"></span>
        <span>@lashvorastudiodemo</span>
      </div>
    </div>
    <div class="address">6812 N.Calder Ridge Ave Beverly Hills , CA 90210</div>
  </section>

</main>
</body>
</html>
```